bramble ledgers
Business cards, letterhead, Comp slip, Accounts front sheet
Bright & Fun-filled
Jake Morrow BSc ACA
Managing Director
4 Hallow Crescent
Lindmere
Castlebrook
EX7 3PD
01392 XXXXXX
jake.morrow@brambleledgers.co.uk
www.brambleledgers.co.uk
Make stand out – perhaps with blue sky and clouds back ground or grass.
Have little icons for phone, email, fax, etc
Comp slip - Same details as letterhead without ifpcs logo or additional wording.
Letterhead - IFPCS logo bottom right.
Letterhead - Wording for the bottom of the page – small, grey.
the bramble ledgers company limited is registered in England and Wales under company number 8314625.
Our registered office is 4 Hallow Crescent, Lindmere, Castlebrook, Redshire, EX7 3PD. A list of directors is available from our registered office.
On the back
Refer a friend and earn 10% of their first year fee! - In a leaf.
Up to 25% off your accounts fee! – In a leaf.
For bottom right of the headed paper only please.

```html
<!DOCTYPE html>
<html lang="en">
<head>
<meta charset="utf-8">
<title>bramble ledgers stationery</title>
<link href="https://fonts.googleapis.com/css2?family=Nunito:wght@400;700;800&family=Great+Vibes&display=swap" rel="stylesheet">
<style>
:root{
  --bg:#ececea;
  --paper:#ffffff;
  --green-dark:#1f6b1e;
  --green:#3f9a22;
  --green-light:#8cc63f;
  --green-pale:#e6f2d8;
  --ink:#3a3a3a;
  --grey:#8a8a8a;
}
*{margin:0;padding:0;box-sizing:border-box}
html,body{width:1200px;height:403px;overflow:hidden;background:var(--bg);font-family:"Nunito",sans-serif;color:var(--ink)}
.canvas{position:relative;width:1200px;height:403px}
.piece{position:absolute;background:var(--paper);box-shadow:0 2px 6px rgba(0,0,0,.25);overflow:hidden}
.brand{font-weight:800;color:var(--green);line-height:1;letter-spacing:-.2px}
.band{position:absolute;left:0;right:0;background:linear-gradient(180deg,var(--green-light),var(--green-dark))}
.band svg{position:absolute;left:0;top:-1px;width:100%;height:14px}

/* business cards */
.card{width:145px;height:74px}
.card-front .brand{position:absolute;left:8px;top:30px;font-size:11px;width:70px}
.card-front .person{position:absolute;right:7px;top:6px;text-align:right;font-size:5px;line-height:1.35;color:var(--ink)}
.card-front .person b{color:var(--green-dark)}
.card-front .band{bottom:0;height:14px}
.card-back{background:linear-gradient(160deg,var(--green-light),var(--green-dark))}
.card-back .offer{position:absolute;left:10px;top:14px;width:80px;padding:6px 8px;border-radius:0 18px 0 18px;background:var(--green-pale);font-size:5.5px;font-weight:700;color:var(--green-dark);line-height:1.3}
.card-back .web{position:absolute;left:0;right:0;bottom:5px;text-align:center;font-size:5px;color:#fff}

/* letterhead */
.letterhead{left:355px;top:22px;width:178px;height:268px}
.letterhead .brand{position:absolute;right:12px;top:14px;font-size:11px;width:72px;text-align:left}
.letterhead .address{position:absolute;right:12px;top:44px;font-size:4px;line-height:1.4;color:var(--grey);text-align:left;width:72px}
.letterhead .footer{position:absolute;left:10px;right:38px;bottom:6px;font-size:3px;line-height:1.35;color:var(--grey)}
.letterhead .badge{position:absolute;right:10px;bottom:6px;width:18px;height:12px;background:#c0392b}

/* envelopes */
.env-front{left:735px;top:20px;width:265px;height:120px}
.env-front .flap{position:absolute;left:0;top:0;width:100%;height:120px}
.env-front .brand{position:absolute;left:16px;top:62px;font-size:9px;width:70px}
.env-back{left:745px;top:92px;width:245px;height:98px}
.env-back .flap{position:absolute;left:0;top:0;width:100%;height:60px}

/* C5 envelope */
.c5{left:542px;top:180px;width:193px;height:146px}
.c5 .flap{position:absolute;left:0;top:0;width:100%;height:42px}
.c5 .brand{position:absolute;right:14px;top:50px;font-size:10px;width:64px}
.c5 .address{position:absolute;left:22px;top:86px;font-size:4px;line-height:1.5;color:var(--ink)}
.c5 .band{bottom:0;height:20px}

/* comp slip */
.comp{left:830px;top:170px;width:170px;height:120px}
.comp .brand{position:absolute;left:10px;top:10px;font-size:8px;width:60px}
.comp .address{position:absolute;right:8px;top:10px;font-size:3.6px;line-height:1.45;color:var(--grey);width:56px}
.comp .greeting{position:absolute;left:10px;right:10px;top:56px;font-family:"Great Vibes",cursive;font-size:22px;color:var(--green-dark);text-align:center}
.comp .band{bottom:0;height:18px}
</style>
</head>
<body>
<main class="canvas">

  <!-- business cards -->
  <section class="piece card card-front" style="left:24px;top:8px">
    <div class="person"><b>Jake Morrow BSc ACA</b><br>Managing Director</div>
    <div class="brand">bramble ledgers</div>
    <div class="band"><svg viewBox="0 0 100 10" preserveAspectRatio="none"><path d="M0 0 Q50 10 100 0 L100 0 Z" fill="#fff"/></svg></div>
  </section>
  <section class="piece card card-front" style="left:185px;top:8px">
    <div class="person"><b>Jake Morrow BSc ACA</b><br>Managing Director</div>
    <div class="brand">bramble ledgers</div>
    <div class="band"><svg viewBox="0 0 100 10" preserveAspectRatio="none"><path d="M0 0 Q50 10 100 0 Z" fill="#fff"/></svg></div>
  </section>
  <section class="piece card card-back" style="left:24px;top:86px">
    <div class="offer">Refer a friend and earn 10% of their first year fee!</div>
    <div class="web">www.brambleledgers.co.uk</div>
  </section>
  <section class="piece card card-back" style="left:185px;top:86px">
    <div class="offer">Up to 25% off your accounts fee!</div>
    <div class="web">www.brambleledgers.co.uk</div>
  </section>

  <!-- letterhead -->
  <section class="piece letterhead">
    <div class="brand">bramble ledgers</div>
    <div class="address">4 Hallow Crescent, Lindmere<br>Castlebrook EX7 3PD<br>01392 XXXXXX<br>jake.morrow@brambleledgers.co.uk<br>www.brambleledgers.co.uk</div>
    <p class="footer">the bramble ledgers company limited is registered in England and Wales under company number 8314625. Our registered office is 4 Hallow Crescent, Lindmere, Castlebrook, Redshire, EX7 3PD. A list of directors is available from our registered office.</p>
    <div class="badge"></div>
  </section>

  <!-- envelopes -->
  <section class="piece env-back">
    <svg class="flap" viewBox="0 0 245 60" preserveAspectRatio="none"><path d="M0 0 H245 V12 L122 60 L0 12 Z" fill="#f4f4f4" stroke="#ddd"/></svg>
  </section>
  <section class="piece env-front">
    <svg class="flap" viewBox="0 0 265 120" preserveAspectRatio="none">
      <defs><linearGradient id="flapGreen" x1="0" y1="0" x2="0" y2="1"><stop offset="0" stop-color="#8cc63f"/><stop offset="1" stop-color="#1f6b1e"/></linearGradient></defs>
      <path d="M0 0 H265 V22 Q132 58 0 22 Z" fill="url(#flapGreen)"/>
    </svg>
    <div class="brand">bramble ledgers</div>
  </section>

  <!-- C5 envelope -->
  <section class="piece c5">
    <svg class="flap" viewBox="0 0 193 42" preserveAspectRatio="none">
      <defs><linearGradient id="c5Green" x1="0" y1="0" x2="0" y2="1"><stop offset="0" stop-color="#1f6b1e"/><stop offset="1" stop-color="#8cc63f"/></linearGradient></defs>
      <path d="M0 0 H193 V18 Q96 46 0 18 Z" fill="url(#c5Green)"/>
    </svg>
    <div class="brand">bramble ledgers</div>
    <div class="address">Jake Morrow<br>4 Hallow Crescent<br>Lindmere<br>Castlebrook<br>EX7 3PD</div>
    <div class="band"><svg viewBox="0 0 100 10" preserveAspectRatio="none"><path d="M0 0 Q50 10 100 0 Z" fill="#fff"/></svg></div>
  </section>

  <!-- comp slip -->
  <section class="piece comp">
    <div class="brand">bramble ledgers</div>
    <div class="address">4 Hallow Crescent, Lindmere<br>Castlebrook EX7 3PD<br>01392 XXXXXX<br>www.brambleledgers.co.uk</div>
    <div class="greeting">With compliments</div>
    <div class="band"><svg viewBox="0 0 100 10" preserveAspectRatio="none"><path d="M0 0 Q50 10 100 0 Z" fill="#fff"/></svg></div>
  </section>

</main>
</body>
</html>
```